New Business Card for Web Design/Internet Marketing Company

Looking for a great looking new business card. We are a 10 year old web design, internet marketing and website management company that works mostly with small businesses.

Our new card needs to better match the colors and style of our website, be bold, extremely usable and slightly edgy.

Target Market(s)

Small/Medium businesses that have websites

Industry/Entity Type

Internet

Requirements
Must have
• Front and back design, full color, rounded corners please

Must use the colors/style of our website (JPG provided)

INFO FOR CARDS (as readable as possible please)
Mark Pellow
President/CEO
mark@brightlanesites.com
Phone: 520-481-7093
Toll Free: 866-481-7093
Address: 4315 E. Kestrel Ave. Ste. 140, Tucson, AZ 85733

THINGS I WANT TO PROMOTE (if there is room):
1. Our Website - www.brightlanesites.com

2. Social Media
Twitter: @brightlanesites
Facebook: www.facebook.com/brightlanesites

3. Our Services
Web Design
Internet Marketing
Website Management

```html
<!DOCTYPE html>
<html lang="en">
<head>
<meta charset="utf-8">
<title>Bright Lane Sites – Business Card</title>
<link href="https://fonts.googleapis.com/css2?family=Ubuntu:wght@300;400;500;700&display=swap" rel="stylesheet">
<style>
  :root{
    --bg:#1c1c1c;
    --orange:#e8671f;
    --blue:#1b72b6;
    --blue-light:#2a8fd4;
    --blue-dark:#1f4f8f;
    --grey:#555a5e;
    --white:#ffffff;
    --paper:#fbfbfb;
  }
  *{box-sizing:border-box;margin:0;padding:0}
  html,body{width:1200px;height:1080px;overflow:hidden}
  body{background:var(--bg);font-family:"Ubuntu",sans-serif;position:relative}

  .card{position:absolute;top:155px;width:440px;height:770px;overflow:hidden}
  .card--front{left:120px;background:var(--paper);border-radius:110px 0 110px 0}
  .card--back{left:640px;background:var(--orange);border-radius:0 110px 0 110px}

  .services{position:absolute;top:0;right:20px;display:flex;gap:3px;height:100%}
  .service{width:22px;display:flex;flex-direction:column;align-items:center}
  .service__bar{width:11px}
  .service__label{writing-mode:vertical-rl;font-size:17px;letter-spacing:1.5px;text-transform:uppercase;margin-top:10px;white-space:nowrap}
  .card--front .service__bar{background:var(--blue)}
  .card--front .service__label{color:var(--grey)}
  .card--back .service__bar{background:var(--white)}
  .card--back .service__label{color:var(--white)}
  .service:nth-child(1) .service__bar{height:100px}
  .service:nth-child(2) .service__bar{height:130px}
  .service:nth-child(3) .service__bar{height:165px}

  .identity{position:absolute;top:108px;left:38px;width:300px}
  .identity__name{font-weight:300;font-size:40px;line-height:1;letter-spacing:-1px;text-transform:uppercase;color:var(--blue);white-space:nowrap}
  .identity__name span{color:var(--orange)}
  .identity__title{font-size:22px;color:var(--grey);text-align:right;margin-top:6px;padding-right:4px}

  .section-title{font-size:27px;font-weight:700;text-transform:uppercase;color:var(--grey);letter-spacing:-.5px}
  .section-title span{color:var(--orange)}

  .contact{position:absolute;top:268px;left:38px}
  .contact__list{list-style:none;margin-top:10px}
  .contact__item{display:flex;font-size:20px;color:var(--grey);line-height:44px;white-space:nowrap}
  .contact__key{color:var(--blue);width:36px;flex:none}
  .contact__item--cont{line-height:32px;margin-top:-6px}

  .social{position:absolute;top:598px;left:38px}
  .social__list{list-style:none;margin-top:10px}
  .social__item{display:flex;align-items:center;font-size:20px;color:var(--grey);line-height:44px}
  .social__mark{width:22px;height:22px;border-radius:3px;margin-right:14px;flex:none}
  .social__mark--a{background:var(--blue-light)}
  .social__mark--b{background:var(--blue-dark)}

  .front-band{position:absolute;left:0;bottom:0;width:110px;height:16px;background:var(--blue)}

  .brand{position:absolute;left:60px;bottom:110px;display:flex;align-items:center;gap:14px}
  .brand__dot{width:26px;height:26px;border-radius:50%;background:var(--white)}
  .brand__name{font-size:34px;font-weight:500;color:var(--white);letter-spacing:-.5px}
</style>
</head>
<body>

<section class="card card--front" aria-label="Card front">
  <div class="services">
    <div class="service"><div class="service__bar"></div><span class="service__label">Web Design</span></div>
    <div class="service"><div class="service__bar"></div><span class="service__label">Internet Marketing</span></div>
    <div class="service"><div class="service__bar"></div><span class="service__label">Website Management</span></div>
  </div>

  <header class="identity">
    <h1 class="identity__name">Mark <span>Pellow</span></h1>
    <p class="identity__title">President/CEO</p>
  </header>

  <div class="contact">
    <h2 class="section-title"><span>Contact</span> Us</h2>
    <ul class="contact__list">
      <li class="contact__item"><span class="contact__key">P.</span>520-481-7093</li>
      <li class="contact__item"><span class="contact__key">T.</span>866-481-7093</li>
      <li class="contact__item"><span class="contact__key">E.</span>mark@brightlanesites.com</li>
      <li class="contact__item"><span class="contact__key">W.</span>www.brightlanesites.com</li>
      <li class="contact__item"><span class="contact__key">A.</span>4315 E. Kestrel Ave.</li>
      <li class="contact__item contact__item--cont"><span class="contact__key"></span>Ste. 140, Tucson, AZ 85733</li>
    </ul>
  </div>

  <div class="social">
    <h2 class="section-title"><span>Social</span> Media</h2>
    <ul class="social__list">
      <li class="social__item"><span class="social__mark social__mark--a"></span>@brightlanesites</li>
      <li class="social__item"><span class="social__mark social__mark--b"></span>/brightlanesites</li>
    </ul>
  </div>

  <div class="front-band"></div>
</section>

<section class="card card--back" aria-label="Card back">
  <div class="services">
    <div class="service"><div class="service__bar"></div><span class="service__label">Web Design</span></div>
    <div class="service"><div class="service__bar"></div><span class="service__label">Internet Marketing</span></div>
    <div class="service"><div class="service__bar"></div><span class="service__label">Website Management</span></div>
  </div>

  <div class="brand">
    <span class="brand__dot"></span>
    <span class="brand__name">Bright Lane Sites</span>
  </div>
</section>

</body>
</html>
```